creation of a business card design for a company specializing in the creation...

I would like to create a design for a professional business card on a black background and with the company's colors (I am attaching some files: including the logo in horizontal and centered format, I am also attaching a recent project design a T-shirt, this is the one I chose to give you an idea of my preferences.

we are in the process of developing a new website design, it is still in the development phase but it can be viewed at the following address: www.vendrelak.be to give you other ideas about the company
you will see for yourself the subject of my main activity: company specializing in the construction of stairs

I would like a business card that stands out from the rest with a unique design

here is the informations
Name: Florent Dubrec
Function: Manager
Address: Rue Masquelin du Pont 41
7180 Haudrimont
telephone: +32 486 219 508
email: info@rv8k.be
website: rv8k. be
social networks: Facebook, YouTube, TikTok, Instagram

Target Market(s)

customer who wants to have a beautiful staircase built

Industry/Entity Type

contruction d'escalier

Contact Information for Business Card

Adresse. Numero de telephone, site web, le texte : "Createur d'escalier", logo recto-verso, icone des reseaux sociaux

Requirements
Must have
• the mention: Stair creator
Nice to have
• an illustration of a designer staircase
Should not have
• do not distort the logo

```html
<!DOCTYPE html>
<html lang="fr">
<head>
<meta charset="utf-8">
<title>RV8K – Cartes de visite</title>
<link rel="stylesheet" href="https://fonts.googleapis.com/css2?family=Bebas+Neue&family=Poppins:wght@300;400;500&display=swap">
<style>
  :root {
    --stage: #2d2d2d;
    --card: #000000;
    --white: #ffffff;
    --blue-light: #94b8d0;
    --blue-mid: #5f8fae;
    --blue-deep: #1f4b66;
    --blue-night: #0f2a3b;
  }
  * { margin: 0; padding: 0; box-sizing: border-box; }
  html, body {
    width: 1200px; height: 1015px; overflow: hidden;
    background: var(--stage);
    font-family: "Poppins", sans-serif;
  }
  .stage {
    width: 1200px; height: 1015px;
    display: flex; flex-direction: column; align-items: center; justify-content: center;
    gap: 44px;
  }
  .card {
    position: relative;
    width: 760px; height: 434px;
    background: var(--card);
    overflow: hidden;
    box-shadow: 0 14px 30px rgba(0,0,0,.45);
  }
  .card__band {
    position: absolute; left: 0; right: 0; bottom: 0; height: 14px;
    background: linear-gradient(90deg, var(--blue-light) 0 55%, var(--blue-mid) 55% 100%);
  }

  /* Front */
  .brand {
    position: absolute; left: 0; right: 0; top: 120px;
    display: flex; align-items: center; justify-content: center; gap: 26px;
  }
  .brand__square { width: 90px; height: 90px; background: var(--blue-mid); }
  .brand__name {
    font-weight: 400; font-size: 104px; line-height: 1;
    letter-spacing: 10px; color: var(--white);
  }
  .socials {
    position: absolute; left: 0; right: 0; top: 300px;
    display: flex; justify-content: center; gap: 12px;
  }
  .socials__dot {
    width: 30px; height: 30px; border-radius: 50%;
    border: 1.5px solid var(--blue-light);
  }

  /* Back */
  .person { position: absolute; left: 56px; top: 92px; }
  .person__name {
    font-family: "Bebas Neue", sans-serif;
    font-size: 46px; line-height: 1; letter-spacing: .5px;
    color: var(--blue-mid);
  }
  .person__role { font-size: 20px; color: var(--white); margin-top: 2px; }
  .contact {
    position: absolute; left: 80px; top: 214px;
    list-style: none; color: var(--white); font-size: 20px; line-height: 30px;
  }
  .contact li { display: flex; align-items: center; gap: 12px; }
  .contact svg { width: 18px; height: 18px; flex: none; }
  .address {
    position: absolute; left: 80px; top: 330px;
    color: var(--white); font-size: 20px; line-height: 28px; font-style: normal;
  }
  .emblem { position: absolute; left: 430px; top: 40px; width: 300px; }
  .emblem__motto {
    font-family: "Bebas Neue", sans-serif;
    font-size: 28px; letter-spacing: 1.5px; color: var(--white);
    text-align: center;
  }
  .emblem__art {
    width: 230px; height: 230px; margin: 6px auto 0; border-radius: 50%;
    background: radial-gradient(circle at 45% 40%, var(--blue-deep) 0%, var(--blue-night) 70%, #0a1a25 100%);
    border: 6px solid var(--blue-deep);
  }
  .emblem__name {
    margin-top: 10px; text-align: center;
    font-size: 48px; line-height: 1; letter-spacing: 6px; color: var(--white);
  }
</style>
</head>
<body>
<main class="stage">

  <section class="card card--front" aria-label="Recto">
    <div class="brand">
      <span class="brand__square"></span>
      <span class="brand__name">RV8K</span>
    </div>
    <div class="socials" aria-label="Réseaux sociaux">
      <span class="socials__dot"></span>
      <span class="socials__dot"></span>
      <span class="socials__dot"></span>
      <span class="socials__dot"></span>
    </div>
    <div class="card__band"></div>
  </section>

  <section class="card card--back" aria-label="Verso">
    <div class="person">
      <h1 class="person__name">FLORENT DUBREC</h1>
      <p class="person__role">Manager</p>
    </div>

    <ul class="contact">
      <li>
        <svg viewBox="0 0 24 24" fill="none" stroke="#5f8fae" stroke-width="2" stroke-linecap="round" stroke-linejoin="round"><path d="M22 16.9v3a2 2 0 0 1-2.2 2 19.8 19.8 0 0 1-8.6-3.1 19.5 19.5 0 0 1-6-6A19.8 19.8 0 0 1 2.1 4.2 2 2 0 0 1 4.1 2h3a2 2 0 0 1 2 1.7c.1.9.4 1.8.7 2.7a2 2 0 0 1-.5 2.1L8 9.8a16 16 0 0 0 6 6l1.3-1.3a2 2 0 0 1 2.1-.4c.9.3 1.8.6 2.7.7a2 2 0 0 1 1.7 2z"/></svg>
        +32 486 219 508
      </li>
      <li>
        <svg viewBox="0 0 24 24" fill="none" stroke="#5f8fae" stroke-width="2" stroke-linejoin="round"><rect x="2" y="5" width="20" height="14"/><path d="M2 5l10 8 10-8"/></svg>
        info@rv8k.be
      </li>
      <li>
        <svg viewBox="0 0 24 24" fill="none" stroke="#5f8fae" stroke-width="2"><circle cx="12" cy="12" r="10"/><path d="M2 12h20M12 2c3 3 3 17 0 20M12 2c-3 3-3 17 0 20"/></svg>
        rv8k. be
      </li>
    </ul>

    <address class="address">
      Rue Masquelin du Pont 41<br>
      7180 Haudrimont
    </address>

    <div class="emblem">
      <p class="emblem__motto">Créateur d'escalier</p>
      <div class="emblem__art" role="img" aria-label="Illustration d'un escalier design aux marches flottantes dans un médaillon bleu"></div>
      <p class="emblem__name">RV8K</p>
    </div>

    <div class="card__band"></div>
  </section>

</main>
</body>
</html>
```